Complete Banner Set For Web Display Ads - Including Zimbly

Ads are driving to a free web class on real estate investing made easy. The offer is for software and training that solves their number 1 challenge - Finding Deals.
Examples of copy suggestions and offer....
"Invest In Real Estate Like A Pro"
"Access Never Before Seen Inventory In Seconds"
"The Country's Best Source For Off-Market Deals"
Brody Halvaney "#1 Real Estate Investing Strategy"
Real Estate

```html
<!DOCTYPE html>
<html lang="en">
<head>
<meta charset="utf-8">
<title>Brody Halvaney – Display Banner Set</title>
<link href="https://fonts.googleapis.com/css2?family=Anton&family=Caveat:wght@600&family=Roboto+Condensed:wght@700&display=swap" rel="stylesheet">
<style>
  :root {
    --canvas: #000000;
    --sky-top: #c4eefa;
    --sky-bottom: #eefafd;
    --orange: #ff7c00;
    --red: #c41e0c;
    --rule: #b3170a;
    --btn-top: #fff27a;
    --btn-bottom: #ffb400;
    --btn-border: #d9340f;
    --ink: #111111;
    --photo-a: #d8dcde;
    --photo-b: #7a5a52;
  }
  * { margin: 0; padding: 0; box-sizing: border-box; }
  html, body { width: 1200px; height: 1200px; overflow: hidden; background: var(--canvas); }
  .canvas { position: relative; width: 1200px; height: 1200px; }

  .banner {
    position: absolute; overflow: hidden;
    background: linear-gradient(180deg, var(--sky-top), var(--sky-bottom));
  }
  .banner > * { position: absolute; }

  .presenter {
    font-family: "Caveat", cursive;
    color: var(--red);
    white-space: nowrap;
    text-align: center;
  }
  .headline {
    font-family: "Anton", "Impact", sans-serif;
    line-height: 1;
    text-align: center;
    white-space: nowrap;
    background: linear-gradient(180deg, var(--orange) 10%, var(--red) 90%);
    -webkit-background-clip: text; background-clip: text;
    color: transparent;
  }
  .rule { height: 2px; background: var(--rule); }

  .portrait {
    background: linear-gradient(180deg, var(--photo-a) 0%, #c9ccce 45%, var(--photo-b) 100%);
    border-radius: 40% 40% 0 0 / 18% 18% 0 0;
  }

  .cta {
    display: flex; align-items: center; justify-content: center;
    border: 3px solid var(--btn-border);
    border-radius: 999px;
    background: linear-gradient(180deg, var(--btn-top), var(--btn-bottom));
    font-family: "Roboto Condensed", "Arial Narrow", sans-serif;
    font-weight: 700; color: var(--ink);
    box-shadow: 0 2px 3px rgba(0,0,0,.25);
  }
  .pointer { overflow: visible; fill: none; stroke: var(--btn-border); stroke-width: 2.5; stroke-linecap: round; stroke-linejoin: round; }
</style>
</head>
<body>
<div class="canvas">

  <!-- 160 x 600 skyscraper -->
  <section class="banner skyscraper" style="left:163px;top:137px;width:160px;height:600px;">
    <p class="presenter" style="left:0;width:160px;top:14px;font-size:21px;">Brody Halvaney</p>
    <p class="headline" style="left:0;width:160px;top:52px;font-size:68px;">#1</p>
    <p class="headline" style="left:0;width:160px;top:125px;font-size:33px;">Real</p>
    <p class="headline" style="left:0;width:160px;top:162px;font-size:33px;">Estate</p>
    <p class="headline" style="left:0;width:160px;top:199px;font-size:33px;">Investing</p>
    <p class="headline" style="left:0;width:160px;top:236px;font-size:33px;">Strategy</p>
    <div class="rule" style="left:21px;width:118px;top:275px;"></div>
    <div class="portrait" role="img" aria-label="Photo of the presenter in a light blazer" style="left:32px;top:285px;width:128px;height:315px;"></div>
    <svg class="pointer" style="left:0;top:520px;" width="160" height="40">
      <path d="M0 10 Q22 8 38 24"/><path d="M30 24 L38 24 L36 16"/>
      <path d="M160 2 Q148 24 128 30"/><path d="M133 24 L128 30 L135 33"/>
    </svg>
    <div class="cta" style="left:5px;top:549px;width:150px;height:38px;font-size:18px;">Click Here</div>
  </section>

  <!-- 336 x 280 large rectangle -->
  <section class="banner rect-large" style="left:353px;top:457px;width:336px;height:280px;">
    <p class="presenter" style="left:0;width:214px;top:10px;font-size:22px;">Brody Halvaney</p>
    <p class="headline" style="left:0;width:216px;top:40px;font-size:42px;">#1</p>
    <p class="headline" style="left:0;width:216px;top:82px;font-size:40px;">Real Estate</p>
    <p class="headline" style="left:0;width:216px;top:126px;font-size:35px;">Investing</p>
    <p class="headline" style="left:0;width:216px;top:164px;font-size:35px;">Strategy</p>
    <div class="rule" style="left:43px;width:132px;top:207px;"></div>
    <div class="portrait" role="img" aria-label="Photo of the presenter in a light blazer" style="left:222px;top:6px;width:114px;height:274px;"></div>
    <svg class="pointer" style="left:0;top:222px;" width="336" height="58">
      <path d="M0 4 Q16 6 28 18"/><path d="M20 18 L28 18 L26 10"/>
      <path d="M196 58 Q184 48 170 42"/><path d="M176 40 L170 42 L174 48"/>
    </svg>
    <div class="cta" style="left:18px;top:219px;width:200px;height:50px;font-size:24px;">Click Here</div>
  </section>

  <!-- 300 x 250 medium rectangle -->
  <section class="banner rect-medium" style="left:730px;top:487px;width:300px;height:250px;">
    <p class="presenter" style="left:0;width:196px;top:8px;font-size:20px;">Brody Halvaney</p>
    <p class="headline" style="left:0;width:196px;top:38px;font-size:36px;">#1</p>
    <p class="headline" style="left:0;width:196px;top:74px;font-size:36px;">Real Estate</p>
    <p class="headline" style="left:0;width:196px;top:113px;font-size:32px;">Investing</p>
    <p class="headline" style="left:0;width:196px;top:147px;font-size:32px;">Strategy</p>
    <div class="rule" style="left:37px;width:120px;top:187px;"></div>
    <div class="portrait" role="img" aria-label="Photo of the presenter in a light blazer" style="left:198px;top:6px;width:102px;height:244px;"></div>
    <svg class="pointer" style="left:0;top:196px;" width="300" height="54">
      <path d="M0 4 Q14 6 24 16"/><path d="M17 16 L24 16 L23 9"/>
      <path d="M176 54 Q166 46 154 40"/><path d="M160 38 L154 40 L158 46"/>
    </svg>
    <div class="cta" style="left:14px;top:195px;width:181px;height:45px;font-size:22px;">Click Here</div>
  </section>

  <!-- 468 x 58 banner -->
  <section class="banner banner-small" style="left:163px;top:789px;width:468px;height:58px;">
    <p class="presenter" style="left:2px;top:7px;font-size:12.5px;">Brody Halvaney</p>
    <p class="headline" style="left:74px;top:3px;font-size:22px;letter-spacing:0.6px;">#1 Real Estate</p>
    <p class="headline" style="left:54px;top:27px;font-size:22px;letter-spacing:0.6px;">Investing Strategy</p>
    <div class="rule" style="left:147px;width:80px;top:52px;"></div>
    <div class="portrait" role="img" aria-label="Photo of the presenter" style="left:275px;top:2px;width:56px;height:56px;"></div>
    <svg class="pointer" style="left:336px;top:0;" width="40" height="30">
      <path d="M2 0 Q8 14 30 24"/><path d="M24 26 L30 24 L27 18"/>
    </svg>
    <div class="cta" style="left:355px;top:16px;width:108px;height:28px;font-size:13px;border-width:2px;">Click Here</div>
  </section>

  <!-- 728 x 90 leaderboard -->
  <section class="banner leaderboard" style="left:163px;top:881px;width:728px;height:90px;">
    <p class="presenter" style="left:3px;top:12px;font-size:19px;">Brody Halvaney</p>
    <p class="headline" style="left:113px;top:5px;font-size:35px;letter-spacing:1.2px;">#1 Real Estate</p>
    <p class="headline" style="left:83px;top:41px;font-size:35px;letter-spacing:1px;">Investing Strategy</p>
    <div class="rule" style="left:227px;width:126px;top:82px;"></div>
    <div class="portrait" role="img" aria-label="Photo of the presenter" style="left:430px;top:1px;width:88px;height:89px;"></div>
    <svg class="pointer" style="left:524px;top:0;" width="60" height="44">
      <path d="M2 0 Q12 24 52 38"/><path d="M45 40 L52 38 L48 31"/>
    </svg>
    <div class="cta" style="left:552px;top:25px;width:168px;height:42px;font-size:20px;">Click Here</div>
  </section>

</div>
</body>
</html>
```